Home Delivery Startup needs a web design!

Hello,
We're a start-up company in the final mile logistics industry. Our name is Brightwater Freight Collective. We partner with retailers throughout the USA and Canada and can perform the following services:
Home Delivery
Warehousing
Assembly
We like grey tones and an ability to incorporate our logo and it's colors throughout the site.
We pride ourselves as being a customizable logistics solution .
Our=comprehensive customer support and advanced technology systems make us distinguishable for every delivery solution.
Strategically located distribution centers throughout North America give us an advantage to get product to customers quickly, safely and conveniently, with consistent, efficient service.
Target Market(s)
Retailers in the US and Canada
Industry/Entity Type
Industry
Coding
Coded - Design and coding required
Number of Pages Required
5+ page

```html
<!DOCTYPE html>
<html lang="en">
<head>
<meta charset="utf-8">
<title>Brightwater Freight Collective</title>
<link rel="stylesheet" href="https://fonts.googleapis.com/css2?family=Ubuntu:wght@400;500;700&display=swap">
<style>
  :root {
    --ink-dark: #1d1d1f;
    --header-dark: #222326;
    --brand-blue: #0b3c96;
    --brand-navy: #0a1f45;
    --brand-red: #e2001c;
    --white: #ffffff;
    --overlay: rgba(40, 40, 40, 0.78);
    --footer-text: #e8e8e8;
  }
  * { box-sizing: border-box; margin: 0; padding: 0; }
  html, body { width: 1200px; height: 2375px; overflow: hidden; }
  body {
    position: relative;
    background: var(--white);
    font-family: "Ubuntu", Arial, sans-serif;
    color: var(--white);
  }

  /* Header */
  .site-header {
    position: absolute; left: 0; top: 0; width: 1200px; height: 92px;
    background: var(--header-dark);
  }
  .brand {
    position: absolute; left: 200px; top: 35px;
    display: flex; align-items: center; gap: 8px;
    font-size: 16px; font-weight: 500; color: var(--white); white-space: nowrap;
  }
  .brand-dot { width: 14px; height: 14px; border-radius: 50%; background: var(--brand-red); flex: none; }
  .main-nav {
    position: absolute; left: 492px; top: 38px;
    display: flex; gap: 24px; list-style: none;
    font-size: 12px; font-weight: 500; white-space: nowrap;
  }
  .region-switch { position: absolute; left: 932px; top: 39px; display: flex; gap: 16px; }
  .region-switch span { width: 20px; height: 13px; background: #c9ced8; display: block; }
  .region-switch span + span { background: #e8c4c4; }

  /* Hero */
  .hero {
    position: absolute; left: 0; top: 92px; width: 1200px; height: 556px;
    background: linear-gradient(180deg, #3a3d5c 0%, #8a6a6e 30%, #c88a5e 45%, #3d3a4a 60%, #1b1e2a 100%);
  }
  .hero-text { position: absolute; left: 0; top: 268px; width: 1200px; text-align: center; }
  .hero-kicker { font-size: 27px; font-weight: 400; }
  .hero-title { font-size: 42px; font-weight: 500; margin-top: 2px; }
  .hero-dots { position: absolute; top: 511px; left: 563px; display: flex; gap: 13px; }
  .hero-dots span { width: 9px; height: 9px; border-radius: 50%; border: 1.5px solid var(--white); }
  .hero-dots span:first-child { border-color: var(--brand-red); }

  /* Welcome */
  .welcome {
    position: absolute; left: 0; top: 648px; width: 1200px; height: 314px;
    background: var(--brand-blue); text-align: center;
  }
  .welcome h1 { font-size: 29px; font-weight: 500; margin-top: 55px; }
  .welcome p {
    width: 770px; margin: 26px auto 0; font-size: 11.2px; line-height: 24px;
  }
  .btn {
    display: inline-block; background: var(--brand-red); color: var(--white);
    font-weight: 500; text-decoration: none; text-align: center; white-space: nowrap;
  }
  .welcome .btn { margin-top: 22px; width: 182px; height: 46px; line-height: 46px; font-size: 18px; }

  /* Services grid */
  .services {
    position: absolute; left: 211px; top: 1031px; width: 778px; height: 632px;
    display: grid; grid-template-columns: 389px 389px; grid-template-rows: 316px 316px;
  }
  .service-cell { position: relative; overflow: hidden; }
  .services-intro { background: var(--brand-red); }
  .services-intro .decor {
    position: absolute; right: 0; top: 30px; width: 200px; height: 200px;
    background: radial-gradient(circle, #bf0017 0%, #c90019 55%, rgba(226,0,28,0) 70%);
  }
  .services-intro h2 {
    position: absolute; left: 26px; top: 194px;
    font-size: 49px; font-weight: 500; line-height: 47px;
  }
  .photo { position: absolute; inset: 0; }
  .photo-warehouse { background: linear-gradient(135deg, #6b5a4c 0%, #8a7767 50%, #4d4239 100%); }
  .photo-courier { background: linear-gradient(160deg, #c9a57c 0%, #d26a2a 55%, #3a5c9a 100%); }
  .photo-racking { background: linear-gradient(160deg, #8f8d88 0%, #b8a98f 50%, #5e5c58 100%); }
  .warehousing-overlay { position: absolute; inset: 0; background: rgba(30, 30, 30, 0.6); }
  .warehousing-text { position: absolute; left: 42px; top: 80px; width: 320px; }
  .warehousing-text h3 { font-size: 28px; font-weight: 500; }
  .warehousing-text p { font-size: 13.4px; line-height: 24.5px; margin-top: 10px; }
  .warehousing-text .btn {
    background: var(--brand-blue); width: 112px; height: 34px; line-height: 34px;
    font-size: 14px; margin-top: 12px;
  }
  .service-band {
    position: absolute; left: 0; bottom: 0; width: 100%; height: 101px;
    background: var(--overlay);
    display: flex; align-items: center; justify-content: space-between;
    padding: 0 22px 0 22px;
  }
  .service-band h3 { font-size: 28px; font-weight: 500; line-height: 30px; }
  .service-band.assembly { padding-left: 42px; }

  /* Map promo */
  .promo {
    position: absolute; left: 211px; top: 1683px; width: 778px; height: 398px;
    background: var(--brand-blue);
  }
  .promo-map {
    position: absolute; left: 390px; top: 0; width: 388px; height: 398px;
    background: radial-gradient(ellipse at 55% 45%, var(--brand-navy) 0%, #0b2a66 55%, rgba(11,60,150,0) 80%);
  }
  .promo h2 {
    position: absolute; left: 26px; top: 22px;
    font-size: 60px; font-weight: 500; line-height: 62px;
  }
  .promo .btn {
    position: absolute; left: 30px; top: 244px; width: 234px; height: 59px;
    line-height: 59px; font-size: 27px;
  }

  /* Footer */
  .site-footer {
    position: absolute; left: 0; top: 2147px; width: 1200px; height: 228px;
    background: var(--ink-dark); color: var(--footer-text);
  }
  .footer-heading { position: absolute; top: 30px; font-size: 14px; font-weight: 500; }
  .quick-links { position: absolute; left: 213px; top: 82px; display: grid; grid-template-columns: 132px 100px; row-gap: 8px; list-style: none; font-size: 11px; font-weight: 500; }
  .newsletter { position: absolute; left: 520px; top: 83px; display: flex; }
  .newsletter span.field {
    width: 182px; height: 32px; background: var(--white); color: #777;
    font-size: 9px; line-height: 32px; padding-left: 7px;
  }
  .newsletter span.submit {
    width: 84px; height: 32px; background: var(--brand-red); color: var(--white);
    font-size: 11px; font-weight: 700; line-height: 32px; text-align: center;
  }
  .social { position: absolute; left: 881px; top: 86px; display: flex; gap: 8px; }
  .social span { width: 24px; height: 24px; border-radius: 50%; display: block; background: #3b5a9a; }
  .social span + span { background: #35a8dc; }
  .copyright {
    position: absolute; left: 0; top: 182px; width: 1200px; text-align: center;
    font-size: 11px; font-weight: 700;
  }
</style>
</head>
<body>

<header class="site-header">
  <div class="brand"><span class="brand-dot"></span>Brightwater Freight Collective</div>
  <ul class="main-nav">
    <li>Home</li><li>About Us</li><li>Services</li><li>FAQ's</li><li>Clients</li><li>Contact Us</li>
  </ul>
  <div class="region-switch" aria-label="Region: USA and Canada"><span></span><span></span></div>
</header>

<section class="hero" role="img" aria-label="City skyline at sunset with a tall lit tower">
  <div class="hero-text">
    <div class="hero-kicker">Strategically located distribution centers throughout</div>
    <div class="hero-title">North America</div>
  </div>
  <div class="hero-dots"><span></span><span></span><span></span><span></span></div>
</section>

<section class="welcome">
  <h1>Welcome To Brightwater Freight Collective</h1>
  <p>Lorem Ipsum is simply dummy text of the printing and typesetting industry. Lorem Ipsum has been the industry's standard dummy text ever since the 1500s, when an unknown printer took a galley of type and scrambled it to make a type specimen book. It has survived not only five centuries, but also the leap into electronic typesetting, remaining essentially unchanged. It was popularised in the 1960s with the release of Lettersheet sheets containing Lorem Ipsum passages, and more recently with desktop publishing software like Pagewright including versions of Lorem Ipsum.</p>
  <a class="btn">Learn More</a>
</section>

<section class="services">
  <div class="service-cell services-intro">
    <div class="decor" role="img" aria-label="Large gear decoration"></div>
    <h2>Our<br>Services</h2>
  </div>
  <div class="service-cell">
    <div class="photo photo-warehouse" role="img" aria-label="Warehouse staff handling boxes"></div>
    <div class="warehousing-overlay"></div>
    <div class="warehousing-text">
      <h3>Warehousing</h3>
      <p>Lorem Ipsum is simply dummy text of the printing and typesetting industry. Lorem Ipsum has been the industry's standard dummy text ever since the 1500s, when an unknown printer took</p>
      <a class="btn">Read More</a>
    </div>
  </div>
  <div class="service-cell">
    <div class="photo photo-courier" role="img" aria-label="Delivery courier carrying a parcel"></div>
    <div class="service-band">
      <h3>Home<br>Delivery</h3>
      <svg width="26" height="26" viewBox="0 0 26 26" aria-hidden="true"><circle cx="13" cy="13" r="11" fill="none" stroke="#fff" stroke-width="2.5"/><path d="M7 13h11M13 8l5 5-5 5" fill="none" stroke="#fff" stroke-width="2.5" stroke-linecap="round" stroke-linejoin="round"/></svg>
    </div>
  </div>
  <div class="service-cell">
    <div class="photo photo-racking" role="img" aria-label="Warehouse racking stacked with pallets"></div>
    <div class="service-band assembly">
      <h3>Assembly</h3>
      <svg width="26" height="26" viewBox="0 0 26 26" aria-hidden="true"><circle cx="13" cy="13" r="11" fill="none" stroke="#fff" stroke-width="2.5"/><path d="M7 13h11M13 8l5 5-5 5" fill="none" stroke="#fff" stroke-width="2.5" stroke-linecap="round" stroke-linejoin="round"/></svg>
    </div>
  </div>
</section>

<section class="promo">
  <div class="promo-map" role="img" aria-label="Map of North America"></div>
  <h2>Brightwater<br>Freight</h2>
  <a class="btn">Get Started</a>
</section>

<footer class="site-footer">
  <div class="footer-heading" style="left:211px">Quick Links</div>
  <ul class="quick-links">
    <li>Home</li><li>FAQ's</li><li>About Us</li><li>Clients</li><li>Services</li><li>Contact Us</li>
  </ul>
  <div class="footer-heading" style="left:520px">Sign Up For Newsletter</div>
  <div class="newsletter"><span class="field">Enter Your E-mail Address</span><span class="submit">SUBSCRIBE</span></div>
  <div class="footer-heading" style="left:880px">Connect With Us</div>
  <div class="social" aria-label="Social links"><span></span><span></span></div>
  <div class="copyright">© 2015 Brightwater Freight Collective . All Rights Reserved | Terms &amp; Condition</div>
</footer>

</body>
</html>
```